Breakfast Cafe - The Coral Table

It is for my breakfast and lunch cafe with a hawaiian / beach theme. I am open 7 days a week from 7am to 2pm. We serve traditional American food such as omelettes, pancakes, burgers and sandwiches. I'll upload my old card and my new logo to be used. We have a lot of day to day regulars who eat there during the week, our t-shirts actually say 'Locals Only' on them. Hope this helps. Thanks.

Target Market(s)

anyone who has an appetite!

Industry/Entity Type

American Restaurant

Contact Information for Business Card

4815C Driftwood Shore Road
Long Beach, California
(562) 555-0187

Requirements
Must have
• Address and phone number easily readable.
Nice to have
• beach or tropical theme

```html
<!DOCTYPE html>
<html lang="en">
<head>
<meta charset="utf-8">
<title>The Coral Table – Business Card</title>
<link href="https://fonts.googleapis.com/css2?family=Bebas+Neue&family=Oswald:wght@500;600&display=swap" rel="stylesheet">
<style>
  :root {
    --page: #e4e4e4;
    --sky: #5bbfd6;
    --foam: #ffffff;
    --sand-dark: #e6d2a6;
    --sand: #f6ebcd;
    --ink: #141414;
    --brand-blue: #3fb2d0;
    --wood: #8a5a2b;
  }
  * { margin: 0; padding: 0; box-sizing: border-box; }
  html, body { width: 1200px; height: 960px; overflow: hidden; background: var(--page); }
  .card {
    position: absolute; left: 75px; top: 180px;
    width: 1050px; height: 600px; overflow: hidden;
    background: var(--sand);
  }
  .card-background { position: absolute; inset: 0; width: 100%; height: 100%; }
  .contact, .services, .brand { position: absolute; text-align: center; color: var(--ink); }
  .contact { left: 495px; width: 540px; top: 58px; }
  .contact-address {
    font-family: "Bebas Neue", sans-serif; font-size: 44px; line-height: 42px; letter-spacing: 0.5px;
  }
  .contact-phone {
    font-family: "Oswald", sans-serif; font-weight: 600; font-size: 56px; line-height: 60px; margin-top: 18px;
  }
  .services { left: 555px; width: 420px; top: 365px; }
  .services-title {
    font-family: "Oswald", sans-serif; font-weight: 600; font-size: 52px; line-height: 60px; letter-spacing: 1px;
  }
  .services-hours {
    font-family: "Oswald", sans-serif; font-weight: 500; font-size: 25px; line-height: 40px; margin-top: 12px;
  }
  .services-hours .days { display: inline-block; border-bottom: 2px solid var(--ink); line-height: 36px; }
  .brand { left: 40px; width: 480px; top: 395px; }
  .brand-name {
    font-family: "Oswald", sans-serif; font-weight: 600; font-size: 62px; line-height: 70px;
    color: var(--brand-blue); letter-spacing: 1px;
  }
  .brand-web {
    font-family: "Oswald", sans-serif; font-weight: 500; font-size: 18px; letter-spacing: 5px;
    color: var(--wood); margin-top: 14px;
  }
</style>
</head>
<body>
  <div class="card">
    <svg class="card-background" viewBox="0 0 700 400" preserveAspectRatio="none" aria-hidden="true">
      <rect width="700" height="400" fill="var(--sand)"/>
      <path d="M0 0 H700 V195 C600 200 520 180 420 168 C300 155 180 175 0 185 Z" fill="var(--sky)"/>
      <path d="M0 185 C180 175 300 155 420 168 C520 180 600 200 700 195 V215 C600 222 520 200 420 190 C300 178 180 198 0 205 Z" fill="var(--foam)"/>
      <path d="M0 205 C180 198 300 178 420 190 C520 200 600 222 700 215 V232 C600 240 520 222 420 212 C300 202 180 220 0 226 Z" fill="var(--sand-dark)"/>
    </svg>

    <div class="brand">
      <p class="brand-name">THE CORAL TABLE</p>
      <p class="brand-web">CORALTABLELB.COM</p>
    </div>

    <div class="contact">
      <p class="contact-address">4815C Driftwood Shore<br>Road Long Beach, California</p>
      <p class="contact-phone">(562) 555-0187</p>
    </div>

    <div class="services">
      <p class="services-title">BREAKFAST &amp;<br>LUNCH CAFE</p>
      <p class="services-hours"><span class="days">OPEN 7 DAYS A WEEK FROM</span><br>7AM TO 2PM.</p>
    </div>
  </div>
</body>
</html>
```